Club Heron Benefit COncert

I need a concert poster designed that I can send ready to go to one of the sites (e.g. flyer hub now). The Pertinent information is

What: Club Heron Benefit Concert
Who: Dale & The Iron Mule Rangers Featuring Ray Pellinor
Special Guests Curtis, Tessa Warnock
Master of Ceremonies Priya Dunmore
Stand Up Comedy by The Badger Q. Whisker's Comedy All-Stars

When July 27, doors open at 7 PM
Where: Club Heron 4817 Kestmore Redwood City

Proceeds benefit The Linden Lodge which is dedicated to serving the families of our wounded soldiers

Sponsors
Club Heron, The Valley Trust of the Shore, and Corvells Medical

Reason: Raymond, I'm off the grid on a trip, hard to get wifi...when i am back if you update the stage name for Curtis, we are good... DAle

• I have to verify how curtis wants to be named. You can pull images from
www.Raypellinorvox.com
www.tessawarnockvox.com,
www.valleytrustshorevox.com/
www.clubheronvox.com
www.lindenlodgevox.org
http://www.vidqubestream.com/user/Dalethecoffeehound

https://www.badgerqwhiskersvox.com/

```html
<!DOCTYPE html>
<html lang="en">
<head>
<meta charset="utf-8">
<title>Club Heron Benefit Concert</title>
<link href="https://fonts.googleapis.com/css2?family=Tinos:wght@700&display=swap" rel="stylesheet">
<style>
  :root {
    --green: #2ff22f;
    --cyan: #3ff3f0;
    --red: #ff1f1f;
    --street-top: #8a7468;
    --street-mid: #5e4a42;
    --street-low: #3a3634;
    --stage-top: #2a2422;
    --stage-mid: #14100f;
    --stage-low: #050404;
    --bg: #000;
  }
  * { margin: 0; padding: 0; box-sizing: border-box; }
  html, body { width: 900px; height: 1200px; overflow: hidden; background: var(--bg); }
  .poster {
    position: relative; width: 900px; height: 1200px; overflow: hidden;
    font-family: "Tinos", "Times New Roman", serif; font-weight: 700;
  }
  .photo-street {
    position: absolute; left: 0; top: 0; width: 900px; height: 605px;
    background:
      radial-gradient(ellipse at 62% 30%, rgba(210,200,190,.55), transparent 45%),
      linear-gradient(90deg, #6a2a22 0%, transparent 22%, transparent 78%, #4a2420 100%),
      linear-gradient(180deg, var(--street-top) 0%, var(--street-mid) 55%, var(--street-low) 100%);
  }
  .photo-stage {
    position: absolute; left: 0; top: 605px; width: 900px; height: 595px;
    background:
      radial-gradient(ellipse at 62% 18%, rgba(230,225,215,.35), transparent 40%),
      radial-gradient(ellipse at 18% 55%, rgba(90,70,60,.6), transparent 45%),
      linear-gradient(180deg, var(--stage-top) 0%, var(--stage-mid) 50%, var(--stage-low) 100%);
  }
  .line { position: absolute; white-space: nowrap; line-height: 1; text-shadow: 1px 1px 2px rgba(0,0,0,.6); }
  .green { color: var(--green); }
  .cyan { color: var(--cyan); }
  .red { color: var(--red); }
  .title-arc { position: absolute; left: 0; top: 0; }
  .title-arc text { font-family: "Tinos", "Times New Roman", serif; font-weight: 700; font-size: 54px; fill: var(--green); }
  .doors { left: 32px; top: 182px; font-size: 37px; }
  .date { left: 30px; top: 222px; font-size: 37px; }
  .venue { left: 26px; top: 268px; font-size: 44px; }
  .address { left: 30px; top: 330px; font-size: 33px; }
  .band { left: 24px; top: 406px; font-size: 47px; }
  .featuring { left: 165px; top: 476px; font-size: 47px; }
  .featuring .headliner { font-size: 62px; margin-left: 14px; }
  .guests { left: 30px; top: 572px; font-size: 47px; }
  .emcee { left: 30px; top: 725px; font-size: 37px; }
  .comedy { left: 30px; top: 770px; font-size: 37px; line-height: 1.08; }
  .proceeds { left: 28px; top: 910px; font-size: 47px; }
  .mission { left: 30px; top: 982px; font-size: 14px; }
  .sponsors { left: 30px; top: 1101px; font-size: 14px; line-height: 3; }
  .charity-badge { position: absolute; left: 722px; top: 964px; }
</style>
</head>
<body>
<main class="poster">
  <div class="photo-street" role="img" aria-label="Photo of a guitarist playing an acoustic guitar in a brick-walled city alley"></div>
  <div class="photo-stage" role="img" aria-label="Photo of a pianist performing at a grand piano on a dim stage"></div>

  <svg class="title-arc" width="900" height="220" viewBox="0 0 900 220" aria-label="Club Heron Benefit Concert">
    <defs><path id="arc" d="M160 165 Q460 -60 790 170"/></defs>
    <text><textPath href="#arc" startOffset="50%" text-anchor="middle">Club Heron Benefit Concert</textPath></text>
  </svg>

  <p class="line green doors">Doors open at 7 pm</p>
  <p class="line green date">July 27/2013</p>
  <p class="line green venue">Club Heron</p>
  <p class="line green address">4817 Kestmore Redwood City</p>

  <p class="line cyan band">Dale &amp; The Iron Mule Rangers</p>
  <p class="line cyan featuring">Featuring<span class="headliner">Ray Pellinor</span></p>
  <p class="line cyan guests">Special Guest Curtis , Tessa Warnock</p>

  <p class="line red emcee">Master of Ceremonies: Priya Dunmore</p>
  <p class="line red comedy">Stand up Comedy by the Badger Whisker's<br>Comedy All- Stars</p>

  <p class="line cyan proceeds">Proceeds will go to the Linden Lodge</p>
  <p class="line cyan mission">The linden lodge is dedicated to the serving families of our wounded Soldiers</p>

  <svg class="charity-badge" width="168" height="168" viewBox="0 0 168 168" role="img" aria-label="Charity partner badge">
    <circle cx="84" cy="84" r="80" fill="#1c2f6e" stroke="#c9a640" stroke-width="6"/>
  </svg>

  <p class="line green sponsors">Sponsors are : Club Heron, The Valley Trust of the Shore &amp;<br>Corvells Medical</p>
</main>
</body>
</html>
```